Updated brief for New ecommerce site needs a stunning business card that links to web site.

Updated business card brief. Please refer to the new files uploaded today (the last two) which show the background colour/style that we will be using in our web template for on-line trading, the grey marble concrete look.

Please see if you can use the grey marble background in the business card design in a way so it relates to our web template. It also needs to be transferable to banner ad, chatterbox ad etc.
vantor hub is a NEW eCommerce website which is commencing selling via bidnook & swapcrate, used & damaged mobile phones & accessories, evolving into a full eCommerce store.

We like strong clean lines, use of a circle, in essence this will become our logo as well. Colours strong orange/Black/White The orange stronger than in PixelHerd #8164937 & grey marble as per file attached #274615

We love the use of a circle!! As we are evolving & moving forward this is what the circle represents to us……. ongoing change.

Front side with a circle with vantor hub in a modern font in the middle, vantor is in a strong orange and group is in black or white. On the reverse side, use layout as per Snapwell design from plonk.com. for icon details (not the boarder at top/botto).

This design is to meet www.plonk.com luxe cards specifications
Thank you we look forward to last minute inspiration.

Project Deadline Extended Reason: Hi We need to extend our deadline to ensure we don't rush the design. We are close to getting what we want, however due to work commitments here we need a couple more days to work this through to ensure the concept ties in with our other marketing.Thank you for understanding and your patience.vantorhub Added Tuesday, March 3, 2015

Target Market(s)

Suppliers & business networking

Industry/Entity Type

Business

Contact Information for Business Card

Liam Presk
Director
mob +61 4987 6543
Locked Bag WXYZ 5678 QRS
liam@vantorhub.example.au
www.vantorhub.example.au

Requirements
Must have
• Design to meet www.plonk.com luxe business card specifications
• Colours - orange needs to be bold and strong & /black/white
• Circle with vantor hub in the middle
Nice to have
• Grey marble background incorporated into design in someway so it links with our web page.

```html
<!DOCTYPE html>
<html lang="en">
<head>
<meta charset="utf-8">
<title>vantorhub business card</title>
<link rel="stylesheet" href="https://fonts.googleapis.com/css2?family=Nunito:wght@700;800&display=swap">
<style>
  :root {
    --orange: #f15a24;
    --black: #000000;
    --white: #ffffff;
    --backdrop: #d9d9d9;
  }
  * { box-sizing: border-box; margin: 0; padding: 0; }
  html, body {
    width: 1200px;
    height: 1000px;
    overflow: hidden;
  }
  body {
    position: relative;
    background: var(--backdrop);
    font-family: "Nunito", sans-serif;
  }
  .card {
    position: absolute;
    overflow: hidden;
  }
  .card-front {
    left: 60px;
    top: 60px;
    width: 660px;
    height: 400px;
    background: var(--orange);
  }
  .front-circle {
    position: absolute;
    left: 160px;
    top: 30px;
    width: 340px;
    height: 340px;
    border-radius: 50%;
    background: var(--black);
    display: flex;
    align-items: center;
    justify-content: center;
  }
  .wordmark {
    font-weight: 800;
    letter-spacing: -1px;
    line-height: 1;
  }
  .front-circle .wordmark {
    color: var(--white);
    font-size: 58px;
  }
  .card-back {
    left: 440px;
    top: 520px;
    width: 700px;
    height: 430px;
    background: var(--black);
  }
  .back-circle {
    position: absolute;
    left: -10px;
    top: 230px;
    width: 350px;
    height: 350px;
    border-radius: 50%;
    background: var(--orange);
  }
  .back-wordmark {
    position: absolute;
    left: 8px;
    top: 350px;
    color: var(--white);
    font-size: 56px;
  }
  .contact {
    position: absolute;
    left: 395px;
    top: 50px;
    color: var(--white);
  }
  .contact-name {
    color: var(--orange);
    font-size: 27px;
    font-weight: 800;
    line-height: 1.1;
  }
  .contact-role {
    font-size: 17px;
    font-weight: 800;
    margin-top: 4px;
  }
  .contact-list {
    list-style: none;
    margin-top: 46px;
  }
  .contact-list li {
    display: flex;
    align-items: center;
    height: 40px;
    font-size: 18px;
    font-weight: 800;
  }
  .contact-icon {
    width: 24px;
    height: 24px;
    margin-right: 22px;
    flex: none;
  }
</style>
</head>
<body>
  <section class="card card-front" aria-label="Card front">
    <div class="front-circle">
      <span class="wordmark">vantorhub</span>
    </div>
  </section>

  <section class="card card-back" aria-label="Card back">
    <div class="back-circle"></div>
    <span class="wordmark back-wordmark">vantorhub</span>

    <div class="contact">
      <p class="contact-name">Liam Presk</p>
      <p class="contact-role">Director</p>
      <ul class="contact-list">
        <li>
          <svg class="contact-icon" viewBox="0 0 24 24" aria-hidden="true">
            <rect x="7" y="2" width="10" height="20" rx="2" fill="none" stroke="#f15a24" stroke-width="2"/>
            <rect x="9" y="5" width="6" height="6" fill="#f15a24"/>
            <circle cx="12" cy="17" r="1.5" fill="#f15a24"/>
          </svg>
          +61 4987 6543
        </li>
        <li>
          <svg class="contact-icon" viewBox="0 0 24 24" aria-hidden="true">
            <path d="M8 11V7a4 4 0 0 1 8 0v4" fill="none" stroke="#f15a24" stroke-width="2"/>
            <circle cx="12" cy="16" r="6.5" fill="#f15a24"/>
            <circle cx="12" cy="15.5" r="1.6" fill="#000"/>
            <rect x="11.3" y="16" width="1.4" height="3" fill="#000"/>
          </svg>
          WXYZ 5678 QRS
        </li>
        <li>
          <svg class="contact-icon" viewBox="0 0 24 24" aria-hidden="true">
            <rect x="1" y="5" width="22" height="14" fill="#f15a24"/>
            <path d="M1 5l11 8 11-8M1 19l8-7M23 19l-8-7" fill="none" stroke="#000" stroke-width="1.5"/>
          </svg>
          liam@vantorhub.example.au
        </li>
        <li>
          <svg class="contact-icon" viewBox="0 0 24 24" aria-hidden="true">
            <circle cx="12" cy="12" r="10" fill="none" stroke="#f15a24" stroke-width="2"/>
            <ellipse cx="12" cy="12" rx="4.5" ry="10" fill="none" stroke="#f15a24" stroke-width="1.6"/>
            <path d="M2 12h20M4 7h16M4 17h16" stroke="#f15a24" stroke-width="1.6"/>
          </svg>
          www.vantorhub.example.au
        </li>
      </ul>
    </div>
  </section>
</body>
</html>
```